Chiropractic Flyers to be made more up to date

I have used this series of flyers for my own practice. I would like the graphics to be brought up to date and the name of the doctor and the practice, the address, phone number and date to be removed and a blank box inserted in one place on the flyer that other chiropractors could use to personalize the flyers for their practice. On some of the flyers, this information is in several places. I'd like to have it all in one space so that it would be easy for the doctor to add it in their practice. They all need to be bright and colorful with catchy graphics.

Industry/Entity Type

Doctor

```html
<!DOCTYPE html>
<html lang="en">
<head>
<meta charset="utf-8">
<title>Chiropractic Flyers</title>
<link rel="stylesheet" href="https://fonts.googleapis.com/css2?family=Cinzel:wght@400;500&family=Oswald:wght@300;400;600&display=swap">
<style>
  :root {
    --backdrop: #5b5f66;
    --gold: #c09d18;
    --gold-glow: #f1c95c;
    --red: #b21b2d;
    --red-glow: #e23c55;
    --white: #ffffff;
    --band-top: #ffffff;
    --band-bottom: #e2e2e2;
    --ink: #2e2e2e;
    --ink-soft: #444444;
  }
  * { margin: 0; padding: 0; box-sizing: border-box; }
  html, body { width: 1200px; height: 1000px; overflow: hidden; }
  body { background: var(--backdrop); position: relative; font-family: "Oswald", "Arial Narrow", sans-serif; }

  .flyer {
    position: absolute; top: 109px; width: 547px; height: 772px;
    overflow: hidden; color: var(--white); text-align: center;
    box-shadow: 0 2px 8px rgba(0,0,0,0.35);
  }
  .flyer--performance { left: 38px; background: radial-gradient(circle at 50% 32%, var(--gold-glow) 0%, var(--gold) 48%, var(--gold) 100%); }
  .flyer--celebration { left: 617px; background: radial-gradient(circle at 50% 36%, var(--red-glow) 0%, var(--red) 50%, var(--red) 100%); }

  .flyer__title {
    position: absolute; left: 0; right: 0; top: 30px;
    font-family: "Cinzel", "Times New Roman", serif; font-weight: 400;
    font-size: 60px; letter-spacing: 1px; line-height: 1;
  }
  .flyer__lead { position: absolute; left: 0; right: 0; top: 97px; font-size: 12px; font-weight: 300; }
  .flyer__tagline { position: absolute; left: 0; right: 0; top: 105px; font-size: 21px; font-weight: 600; }
  .flyer__body { position: absolute; left: 70px; right: 70px; font-size: 10.5px; font-weight: 300; line-height: 1.22; }
  .flyer__body--top { top: 120px; }
  .flyer__body--red-top { top: 136px; }

  .flyer__art { position: absolute; }
  .flyer__art--car { left: 92px; top: 235px; width: 378px; height: 172px; border-radius: 60px 90px 30px 30px;
    background: linear-gradient(180deg, #6b6d72 0%, #3a3c40 60%, #1e1f22 100%); }
  .flyer__art--headline { left: 38px; top: 256px; width: 472px; height: 166px; border-radius: 40px;
    background: linear-gradient(180deg, #f4f4f4 0%, #d9d9d9 45%, #c41f33 46%, #9e1424 100%); }

  .offer__heading { position: absolute; left: 0; right: 0; top: 452px; font-size: 32px; font-weight: 600; letter-spacing: 0.3px; }
  .offer__text { position: absolute; left: 40px; right: 40px; top: 499px; font-size: 17px; font-weight: 300; line-height: 1.35; }
  .flyer__note { position: absolute; left: 0; right: 0; font-size: 6.5px; font-weight: 300; }
  .flyer__note--gold { top: 555px; }
  .flyer__note--red { top: 509px; }
  .flyer__message { position: absolute; left: 90px; right: 90px; top: 455px; font-size: 12px; font-weight: 300; line-height: 1.25; }

  .contact-band {
    position: absolute; left: 0; right: 0; top: 609px; height: 163px;
    background: linear-gradient(180deg, var(--band-top) 0%, var(--band-bottom) 100%);
    font-family: "Cinzel", "Times New Roman", serif; color: var(--ink);
  }
  .contact-band__pointer { position: absolute; left: 260px; top: 0; }
  .contact-band__name { position: absolute; left: 0; right: 0; top: 34px; font-size: 45px; font-weight: 400; line-height: 1; }
  .contact-band__address { position: absolute; left: 0; right: 0; top: 88px; font-size: 13px; color: var(--ink-soft); }
  .contact-band__lines { position: absolute; left: 0; right: 0; top: 118px; font-size: 12px; color: var(--ink-soft); }
</style>
</head>
<body>

<section class="flyer flyer--performance">
  <h1 class="flyer__title">PERFORMANCE</h1>
  <p class="flyer__lead">Like a race car, your body functions at a level of peak performance when it is properly tuned.</p>
  <p class="flyer__body flyer__body--top">You can join the hundreds of people who have improved their health and performance through natural, drug-free Chiropractic. Call today to receive your complimentary consultation and examination absolutely FREE!</p>
  <div class="flyer__art flyer__art--car" role="img" aria-label="Photo of a dark grey sports car"></div>
  <h2 class="offer__heading">SPECIAL OFFER:</h2>
  <p class="offer__text">Appointments scheduled within the next 2 weeks will receive their first session of Chiropractic care at NO CHARGE!</p>
  <p class="flyer__note flyer__note--gold">*Offer not valid for Medicare, worker's comp. or personal injury cases.</p>
  <div class="contact-band">
    <svg class="contact-band__pointer" width="28" height="20" viewBox="0 0 28 20" aria-hidden="true">
      <polygon points="0,0 28,0 14,18" fill="var(--gold)" stroke="#d9b43a" stroke-width="1"/>
    </svg>
    <p class="contact-band__name">Doctor’s Name</p>
    <p class="contact-band__address">Address, City, State</p>
    <p class="contact-band__lines">Telephone (555) 123-4567 &nbsp;|&nbsp; Email Name@Domain.com</p>
  </div>
</section>

<section class="flyer flyer--celebration">
  <h1 class="flyer__title">CELEBRATION</h1>
  <p class="flyer__tagline">Bring Family and Friends to Celebrate with Us</p>
  <p class="flyer__body flyer__body--red-top">All exams, treatments, scoliosis screenings, and x-rays (taken if necessary) performed for a nominal charity donation. Plus FREE refreshments!!!</p>
  <div class="flyer__art flyer__art--headline" role="img" aria-label="3D red and white lettering reading Grand Opening!"></div>
  <p class="flyer__message">This will be a great opportunity for us to introduce ourselves to the community... AND For you and your family to take great strides towards better health... AND To support an excellent cause!</p>
  <p class="flyer__note flyer__note--red">*Offer not valid for Medicare, worker's comp. or personal injury cases.</p>
  <div class="contact-band">
    <svg class="contact-band__pointer" width="28" height="20" viewBox="0 0 28 20" aria-hidden="true">
      <polygon points="0,0 28,0 14,18" fill="var(--red)" stroke="#d9b43a" stroke-width="1"/>
    </svg>
    <p class="contact-band__name">Doctor’s Name</p>
    <p class="contact-band__address">Address, City, State</p>
    <p class="contact-band__lines">Telephone (555) 123-4567 &nbsp;|&nbsp; Email Name@Domain.com</p>
  </div>
</section>

</body>
</html>
```